Copper Lantern Gatherings need a stand out marketing flyer.

Copper Lantern Gatherings is a company that runs empowerment retreats and bespoke corporate training in creating positive change.
We would like an A5 flyer that is 2 sided. the reverse side of the flyer we would like some of our testimonial quotes.

The flyer should be punchy and not too heavy with wordy detail but have enough detail so people can see what we offer. Encouraging people to contact us to find out more

Our empowerment retreats help people to live without limits, be fierce and wild, be creative and courageous, be fearless and free.
Leave behind
- lack of self esteem
- lack of personal power
- lack of focus
- old fears and beliefs
- overwhelm
Find new
- confidence
- personal empowerment
- commitment
- courage
- resilience

Contact details:
website: www.copperlanterngatherings.example.co.uk
email: info@copperlanterngatherings.example.com
Rebecca Thornby Tel: 07700 900 318
Joanna Pelling Tel: 07700 900 752

You can use as much of the detail above in your design as you would like..
I attach our logos. you can pick which ever design you prefer to work with. I have also attached a file that contains the testimonials for the reverse of the slide. I've also attached a few pictures but these aren't necessary in your design they are just an option/idea for you to consider. You can use alternative pictures should you wish to.

Details for our up and coming events can be found on our website

```html
<!DOCTYPE html>
<html lang="en">
<head>
<meta charset="utf-8">
<title>Copper Lantern Gatherings – A5 Flyer</title>
<link rel="stylesheet" href="https://fonts.googleapis.com/css2?family=Cinzel:wght@400&family=Montserrat:ital,wght@0,300;0,400;0,600;0,700;1,300;1,700&family=Oswald:wght@600&family=Arimo:wght@400;700&display=swap">
<style>
  :root {
    --board: #aca290;
    --board-base: #ffffff;
    --ink-light: #ffffff;
    --ink-soft: #e8ece9;
    --back-panel: #14231f;
    --rock-dark: #1c2a24;
    --rock-mid: #34453d;
    --rock-warm: #5e4c4a;
    --moss: #4f9a85;
    --foliage: #23301f;
  }
  * { margin: 0; padding: 0; box-sizing: border-box; }
  html, body { width: 1200px; height: 869px; overflow: hidden; }
  body {
    position: relative;
    background: var(--board);
    font-family: "Montserrat", sans-serif;
    color: var(--ink-light);
  }
  .board-base {
    position: absolute; left: 0; top: 848px; width: 1200px; height: 21px;
    background: var(--board-base);
  }
  .board-title {
    position: absolute; top: 40px; left: 0; width: 1200px;
    text-align: center;
    font-family: "Cinzel", serif;
    font-size: 20px; letter-spacing: 1.2px; font-weight: 400;
    color: var(--ink-light);
  }
  .side-label {
    position: absolute; top: 424px;
    font-family: "Cinzel", serif; font-size: 13px; letter-spacing: 1.5px;
    transform: translate(-50%, -50%) rotate(-90deg);
    color: var(--ink-light);
  }
  .side-label--front { left: 56px; }
  .side-label--back { left: 621px; }

  .flyer {
    position: absolute; top: 114px; width: 480px; height: 678px;
    overflow: hidden;
    box-shadow: 4px 5px 8px rgba(0,0,0,.35);
  }
  .flyer--front { left: 91px; }
  .flyer--back { left: 656px; background: var(--back-panel); }

  /* Front */
  .hero-photo {
    position: absolute; inset: 0;
    background:
      radial-gradient(ellipse 40% 18% at 62% 22%, rgba(79,154,133,.55), transparent 70%),
      radial-gradient(ellipse 30% 20% at 35% 55%, rgba(79,154,133,.45), transparent 70%),
      radial-gradient(ellipse 55% 25% at 30% 10%, rgba(94,76,74,.9), transparent 75%),
      linear-gradient(180deg, var(--rock-warm) 0%, var(--rock-mid) 25%, var(--rock-dark) 55%, var(--foliage) 100%);
  }
  .marker { position: absolute; }
  .marker--top { left: 42px; top: 56px; }
  .marker--hand { left: 262px; top: 190px; }

  .rule-v { position: absolute; width: 1px; background: var(--ink-light); }
  .rule-v--find { left: 50px; top: 85px; height: 143px; }
  .rule-v--leave { left: 280px; top: 463px; height: 116px; }

  .find-heading {
    position: absolute; left: 67px; top: 80px;
    font-weight: 700; font-style: italic; font-size: 19px;
  }
  .find-list {
    position: absolute; left: 67px; top: 107px; list-style: none;
    font-weight: 300; font-size: 20px; line-height: 24.5px;
  }
  .leave-heading {
    position: absolute; left: 298px; top: 490px;
    font-weight: 700; font-style: italic; font-size: 11px;
  }
  .leave-list {
    position: absolute; left: 298px; top: 510px; list-style: none;
    font-weight: 400; font-size: 11px; line-height: 13.7px;
  }
  .photo-credit {
    position: absolute; left: 453px; top: 291px;
    transform: translate(-50%, -50%) rotate(-90deg);
    font-size: 6.5px; white-space: nowrap; color: var(--ink-soft);
  }
  .photo-credit b { font-weight: 700; font-style: normal; }
  .photo-credit i { font-style: italic; }

  .brand {
    position: absolute; width: 90px; text-align: center;
    font-family: "Montserrat", sans-serif; font-weight: 600;
    font-size: 9px; line-height: 11px; letter-spacing: .8px;
    text-transform: uppercase; color: var(--ink-light);
  }
  .brand__dot {
    display: block; width: 14px; height: 14px; margin: 0 auto 6px;
    border: 1.5px solid var(--ink-light); border-radius: 50%;
  }
  .flyer--front .brand { left: 36px; top: 568px; }
  .flyer--back .brand { left: 38px; top: 568px; }

  .contact-line {
    position: absolute; top: 629px; left: 118px; right: 22px;
    font-size: 5.6px; letter-spacing: -0.05px; white-space: nowrap;
    text-align: right; color: var(--ink-light);
  }
  .contact-line b { font-weight: 700; }

  /* Back */
  .testimonial-heading {
    position: absolute; top: 40px; left: 0; width: 480px; text-align: center;
    font-weight: 700; font-size: 19px; letter-spacing: .6px;
  }
  .quote-mark {
    position: absolute; font-family: "Arimo", sans-serif; font-weight: 700; line-height: 1;
  }
  .quote-lead {
    position: absolute; left: 98px; top: 111px;
    font-family: "Arimo", sans-serif; font-weight: 700; font-size: 13.5px; line-height: 18px;
  }
  .quote-feature {
    position: absolute; left: 84px; top: 170px;
    font-weight: 300; font-style: italic; font-size: 20px; line-height: 23px;
    letter-spacing: .4px;
  }
  .quote-body {
    position: absolute; left: 61px; width: 360px;
    text-align: justify; text-align-last: left;
    font-weight: 400;
  }
  .quote-body--one { top: 266px; font-size: 12.4px; line-height: 15px; letter-spacing: .7px; }
  .quote-body--two { top: 347px; font-size: 10.2px; line-height: 13px; letter-spacing: .35px; text-align-last: center; }
  .quote-bold {
    position: absolute; left: 90px; top: 404px; width: 300px; text-align: center;
    font-family: "Oswald", sans-serif; font-weight: 600; font-size: 15px; line-height: 22px;
  }
  .quote-body--four {
    top: 471px; font-family: "Arimo", sans-serif; font-size: 12px; line-height: 15px;
    text-align: center; text-align-last: center;
  }
  .rule-h { position: absolute; left: 131px; width: 297px; height: 1px; background: var(--ink-light); }
  .rule-h--top { top: 564px; }
  .rule-h--bottom { top: 617px; }
  .team {
    position: absolute; left: 145px; top: 571px;
    border-collapse: collapse; font-size: 15px; line-height: 21px;
  }
  .team td { padding: 0; white-space: nowrap; }
  .team__name { text-align: right; font-weight: 400; letter-spacing: .5px; }
  .team__sep { padding: 0 8px !important; font-weight: 700; }
  .team__phone { font-weight: 700; letter-spacing: .3px; }
</style>
</head>
<body>
  <h1 class="board-title">Copper Lantern Gatherings Flyer Design (A5 Size)</h1>
  <span class="side-label side-label--front">FRONT</span>
  <span class="side-label side-label--back">BACK</span>

  <section class="flyer flyer--front">
    <div class="hero-photo" role="img" aria-label="Photograph of a woman bouldering up a moss-covered rock face, seen from above"></div>

    <svg class="marker marker--top" width="16" height="16" viewBox="0 0 16 16" aria-hidden="true">
      <circle cx="8" cy="8" r="7" fill="none" stroke="#fff" stroke-width="1.2"/>
      <circle cx="8" cy="8" r="4" fill="none" stroke="#fff" stroke-width="1"/>
    </svg>
    <svg class="marker marker--hand" width="32" height="32" viewBox="0 0 32 32" aria-hidden="true">
      <circle cx="16" cy="16" r="15" fill="rgba(255,255,255,.18)"/>
      <circle cx="16" cy="16" r="12" fill="none" stroke="#fff" stroke-width="1.4"/>
      <circle cx="16" cy="16" r="7" fill="none" stroke="#fff" stroke-width="1.4"/>
      <circle cx="16" cy="16" r="3" fill="#fff"/>
    </svg>

    <span class="rule-v rule-v--find"></span>
    <h2 class="find-heading">FIND NEW :</h2>
    <ul class="find-list">
      <li>Confidence</li>
      <li>Personal Empowerment</li>
      <li>Commitment</li>
      <li>Courage</li>
      <li>Resilience</li>
    </ul>

    <span class="photo-credit"><i>photo by :</i> <b>@fieldlens</b></span>

    <span class="rule-v rule-v--leave"></span>
    <h2 class="leave-heading">LEAVE BEHIND :</h2>
    <ul class="leave-list">
      <li>Lack of self esteem</li>
      <li>Lack of personal power</li>
      <li>Lack of focus</li>
      <li>Old fears and beliefs</li>
      <li>Overwhelm</li>
    </ul>

    <div class="brand"><span class="brand__dot"></span>Copper<br>Lantern<br>Gatherings</div>
    <p class="contact-line"><b>w</b> . www.copperlanterngatherings.example.co.uk &nbsp;|&nbsp; <b>e</b> . info@copperlanterngatherings.example.com</p>
  </section>

  <section class="flyer flyer--back">
    <h2 class="testimonial-heading">TESTIMONIAL</h2>

    <span class="quote-mark" style="left:62px;top:110px;font-size:38px;">&ldquo;</span>
    <p class="quote-lead">Do not hesitate, just book it!<br>It will transform and enhance your life.</p>
    <span class="quote-mark" style="left:390px;top:118px;font-size:38px;">&rdquo;</span>

    <p class="quote-feature">&ldquo;If you have a chance to do it<br>then do it, it&rsquo;s one of the<br>best experience of my life.&rdquo;</p>

    <p class="quote-body quote-body--one">&ldquo; I&rsquo;ve met the most amazing people &amp; feel like I am well equipped with the tools now to help myself physically and mentally. The best self-care I&rsquo;ve ever invested in.&rdquo;</p>

    <p class="quote-body quote-body--two">&ldquo; It&rsquo;s changed my life, given me perspective and time to develop myself. I&rsquo;ve met the most amazing people and learnt so much. It&rsquo;s worth every penny. &rdquo;</p>

    <span class="quote-mark" style="left:69px;top:398px;font-size:24px;">&ldquo;</span>
    <p class="quote-bold">The most wonderful weekend of self-discovery<br>and would recommend it to everyone.</p>
    <span class="quote-mark" style="left:392px;top:416px;font-size:24px;">&rdquo;</span>

    <p class="quote-body quote-body--four">&ldquo; I can&rsquo;t thank Copper Lantern enough for the tools they have<br>metaphorically equipped me with. They are amazing at what<br>they do.&rdquo;</p>

    <div class="brand"><span class="brand__dot"></span>Copper<br>Lantern<br>Gatherings</div>

    <span class="rule-h rule-h--top"></span>
    <table class="team">
      <tr><td class="team__name">Rebecca Thornby</td><td class="team__sep">:</td><td class="team__phone">07700 900 318</td></tr>
      <tr><td class="team__name">Joanna Pelling</td><td class="team__sep">:</td><td class="team__phone">07700 900 752</td></tr>
    </table>
    <span class="rule-h rule-h--bottom"></span>
    <p class="contact-line"><b>w</b> . www.copperlanterngatherings.example.co.uk &nbsp;|&nbsp; <b>e</b> . info@copperlanterngatherings.example.com</p>
  </section>

  <div class="board-base"></div>
</body>
</html>
```